Business Card Design

Selling Televisions, Velmora, Kira, Dravelux, Ronavi
The latest models, sizes ranging from 22"- 75"
Surround Sounds, Sound Bars and Wall Mounts

Target Market(s)

Mainly males/boys/blokes etc

Industry/Entity Type

Business

Contact Information for Business Card

Glen Marsh
07841526094
glmarsh@quinvale-mail.com

Requirements
Must have
• simplistic design, probably just 2 of the images used

clarity essential
Nice to have
• Metallic if possible

```html
<!DOCTYPE html>
<html lang="en">
<head>
<meta charset="utf-8">
<title>Glen Marsh – Business Card</title>
<link rel="stylesheet" href="https://fonts.googleapis.com/css2?family=Syncopate:wght@400;700&family=Michroma&family=Oswald:wght@500&display=swap">
<style>
  :root {
    --frame: #000000;
    --metal-light: #b4bcbc;
    --metal-mid: #6c7676;
    --metal-dark: #182020;
    --streak-light: rgba(255,255,255,0.10);
    --streak-dark: rgba(0,0,0,0.12);
    --shelf: #1a1a1a;
    --shelf-edge: #3a3a3a;
    --ink: #ffffff;
    --screen-light: #c9cfcf;
    --screen-dark: #7d8787;
  }
  html, body {
    margin: 0;
    padding: 0;
    overflow: hidden;
    background: var(--frame);
  }
  .card {
    position: relative;
    width: 1200px;
    height: 791px;
    background: var(--frame);
    overflow: hidden;
  }
  .card__panel {
    position: absolute;
    left: 48px;
    top: 40px;
    width: 1107px;
    height: 711px;
    background:
      repeating-linear-gradient(180deg,
        var(--streak-light) 0px, transparent 1px, transparent 2px,
        var(--streak-dark) 3px, transparent 4px, transparent 5px,
        var(--streak-light) 6px, transparent 7px, var(--streak-dark) 9px, transparent 10px),
      repeating-linear-gradient(180deg,
        transparent 0px, rgba(255,255,255,0.06) 13px, transparent 17px,
        rgba(0,0,0,0.08) 29px, transparent 37px),
      repeating-linear-gradient(90deg,
        transparent 0px, rgba(255,255,255,0.04) 41px, transparent 97px,
        rgba(0,0,0,0.05) 163px, transparent 221px),
      radial-gradient(ellipse 60% 55% at 50% 48%, var(--metal-light) 0%, var(--metal-mid) 55%, var(--metal-dark) 100%);
    box-shadow: inset 0 0 60px 20px rgba(0,0,0,0.85);
  }
  .tv {
    position: absolute;
    border-radius: 4px;
    box-shadow: 0 0 0 3px rgba(255,255,255,0.85), 0 4px 8px rgba(0,0,0,0.45);
  }
  .tv--centre {
    left: 367px; top: 79px; width: 467px; height: 273px;
    background: linear-gradient(180deg, var(--screen-light), var(--screen-dark));
  }
  .tv--left {
    left: 58px; top: 179px; width: 289px; height: 251px;
    background: linear-gradient(90deg, var(--screen-light), var(--screen-dark));
  }
  .tv--right {
    left: 851px; top: 179px; width: 292px; height: 251px;
    background: linear-gradient(270deg, var(--screen-light), var(--screen-dark));
  }
  .shelf {
    position: absolute;
    left: 0; top: 0;
    width: 1200px; height: 791px;
    pointer-events: none;
  }
  .contact {
    position: absolute;
    left: 0;
    width: 1200px;
    text-align: center;
    color: var(--ink);
    text-shadow: 2px 3px 4px rgba(0,0,0,0.8);
    white-space: nowrap;
  }
  .contact__name {
    top: 500px;
    margin: 0;
    font-family: "Syncopate", "Michroma", sans-serif;
    font-weight: 400;
    font-size: 64px;
    line-height: 76px;
    font-variant: small-caps;
    letter-spacing: 4px;
  }
  .contact__phone {
    top: 604px;
    font-family: "Oswald", sans-serif;
    font-weight: 500;
    font-size: 36px;
    line-height: 44px;
    letter-spacing: 4px;
  }
  .contact__email {
    top: 670px;
    font-family: "Oswald", sans-serif;
    font-weight: 500;
    font-size: 42px;
    line-height: 52px;
    letter-spacing: 1px;
  }
</style>
</head>
<body>
  <div class="card">
    <div class="card__panel"></div>

    <div class="tv tv--left" role="img" aria-label="Outline of a curved television angled to the left"></div>
    <div class="tv tv--centre" role="img" aria-label="Outline of a flat-screen television on a stand"></div>
    <div class="tv tv--right" role="img" aria-label="Outline of a curved television angled to the right"></div>

    <svg class="shelf" viewBox="0 0 1200 791" aria-hidden="true">
      <defs>
        <filter id="shelf-shadow" x="-10%" y="-30%" width="120%" height="170%">
          <feDropShadow dx="4" dy="10" stdDeviation="8" flood-color="#000" flood-opacity="0.6"/>
        </filter>
      </defs>
      <polygon filter="url(#shelf-shadow)"
        points="364,416 837,416 961,502 947,536 812,452 388,452 226,536 210,502"
        fill="var(--shelf)" stroke="var(--shelf-edge)" stroke-width="2"/>
    </svg>

    <h1 class="contact contact__name">Glen Marsh</h1>
    <div class="contact contact__phone">07841526094</div>
    <div class="contact contact__email">glmarsh@quinvale-mail.com</div>
  </div>
</body>
</html>
```